Whitepaper: 7 Keys to Achieving Success of Your RTLS Initiative

Create a graphical layout for a whitepaper that would include 7 illustrations matching each subject line. Colors aligned with Boundless Stride branding guide (attached)

Just to summarize, I would need graphics/illustrations for 7 bullet points - Key #1: Set Measurements for Success Key #2: Establish a Clear Roadmap Key #3: Don’t Use Pilots (small try out of software) Key #4: Plan for the Future, from the Start Key #5: Think about RTLS as an Initiative, not a Project Key #6: Nurture the Change Key #7: Show Successes, Early

I would expect about 2-3 illustrations per page. Format - US size 8.5x11. PDF file, but would like to have the ability to edit text if needed. Thank you for your interest. Colors don't need to match the branding. It is a healthcare whitepaper so it could be blue and green.

Reason: Some of you have asked for a time extension.

```html
<!DOCTYPE html>
<html lang="en">
<head>
<meta charset="UTF-8">
<title>7 Keys to Achieving Success of Your RTLS Initiative</title>
<link rel="stylesheet" href="https://fonts.googleapis.com/css2?family=Montserrat:wght@700&family=Raleway:wght@400&display=swap">
<style>
  :root {
    --brand-red: #c00000;
    --body-grey: #555555;
    --paper: #ffffff;
  }
  html, body {
    margin: 0;
    padding: 0;
    overflow: hidden;
    background: var(--paper);
  }
  .page {
    position: relative;
    width: 927px;
    height: 1200px;
    overflow: hidden;
    background: var(--paper);
  }
  .key-icon {
    position: absolute;
    left: 398px;
    width: 144px;
    height: 144px;
    border-radius: 50%;
    background: var(--brand-red);
  }
  .key-icon svg {
    width: 144px;
    height: 144px;
    display: block;
  }
  .key-title {
    position: absolute;
    margin: 0;
    left: 0;
    width: 927px;
    text-align: center;
    font-family: "Montserrat", sans-serif;
    font-weight: 700;
    font-size: 24px;
    line-height: 43px;
    color: var(--brand-red);
  }
  .key-text {
    position: absolute;
    margin: 0;
    font-family: "Raleway", sans-serif;
    font-weight: 400;
    font-size: 17px;
    line-height: 32.8px;
    color: var(--body-grey);
    text-align: justify;
    text-align-last: left;
  }
  .key-one .key-icon { top: 111px; }
  .key-one .key-title { top: 297px; }
  .key-one .key-text { top: 358px; left: 119px; width: 702px; }
  .key-two .key-icon { top: 656px; }
  .key-two .key-title { top: 825px; }
  .key-two .key-text { top: 929px; left: 128px; width: 683px; }
</style>
</head>
<body>
<main class="page">
  <section class="key key-one">
    <div class="key-icon">
      <svg viewBox="0 0 144 144" aria-hidden="true">
        <path d="M66 52 a6 6 0 0 1 12 0 v38 a14 14 0 1 1 -12 0 z" fill="none" stroke="#fff" stroke-width="3.5" stroke-linejoin="round"/>
        <line x1="72" y1="60" x2="72" y2="96" stroke="#fff" stroke-width="3.5" stroke-linecap="round"/>
        <circle cx="72" cy="102" r="6" fill="#fff"/>
      </svg>
    </div>
    <h2 class="key-title">Key #1: Set Measurements for RTLS Success</h2>
    <p class="key-text">You cannot claim a success if you don’t define what success means to your organization. You need to work with your executive team to establish a clear vision of what RTLS is going to do for you and agree on the expected return on investment (ROI) for this technology. I have to add that as someone who is a part of the executive team myself, I don’t really care how much something costs. What I care about is how much value does it bring back to the organization for that cost.</p>
  </section>

  <section class="key key-two">
    <div class="key-icon">
      <svg viewBox="0 0 144 144" aria-hidden="true">
        <path d="M55 93 C44 80 37 70 37 60 a18 18 0 0 1 36 0 c0 10 -7 20 -18 33 z" fill="none" stroke="#fff" stroke-width="3.5" stroke-linejoin="round"/>
        <circle cx="55" cy="60" r="8" fill="none" stroke="#fff" stroke-width="3.5"/>
        <path d="M60 101 C72 112 95 110 100 100 C104 90 90 88 91 78 C92 72 98 68 112 53" fill="none" stroke="#fff" stroke-width="3" stroke-linecap="round" stroke-dasharray="4 6"/>
      </svg>
    </div>
    <h2 class="key-title">Key #2: Establish a Clear Roadmap for an RTLS<br>Deployment</h2>
    <p class="key-text">It is not uncommon that you will come up with 10, 50, or even 100 different projects and problems that can be solved with RTLS technology. However, in order to actually act on all of those opportunities you really need a clear roadmap of which use cases and in what particular order you want to implement them to get the fastest ROI and the best utilization of your resources.</p>
  </section>
</main>
</body>
</html>
```